Business Card Design Project

We require business cards to be produced with the following design
http://files.pixelvault-demo.net/img/50329/84172/84172_2093548_50329_image.jpg
Rather than bright meadow, please use Vantelo as the comapny name.
Please also use the following contact details:
1.
Daniel Overbeck
Entrepreneur
07423158871
doverbeck@vantelo-demo.com
2.
Tom Ashworth
Founder
07539402217
tashworth@vantelo-demo.com
Please add:
friendhub favicion facebook.com/vantelo
Linked in favicon linkedin/danieloverbeck
callspot favicon doverbeck
Linked in favicon linkedin/thomasashworth
callspot favicon thomasashworth
circle talk favicon tomashworth@mailbox-demo.net
To the back

```html
<!DOCTYPE html>
<html lang="en">
<head>
<meta charset="utf-8">
<title>Vantelo Business Cards</title>
<link rel="stylesheet" href="https://fonts.googleapis.com/css2?family=Source+Sans+3:wght@400&family=Arimo:wght@700&display=swap">
<style>
  :root {
    --brand-red: #ed1c24;
    --ink-grey: #808080;
    --label-grey: #6d6e71;
    --card-border: #231f20;
    --paper: #ffffff;
  }
  html, body {
    margin: 0;
    padding: 0;
    width: 1035px;
    height: 1200px;
    overflow: hidden;
    background: var(--paper);
  }
  .sheet {
    position: relative;
    width: 1035px;
    height: 1200px;
    font-family: "Source Sans 3", "Myriad Pro", sans-serif;
    color: var(--ink-grey);
  }
  .card {
    position: absolute;
    left: 25px;
    width: 990px;
    height: 577px;
    border: 1.5px solid var(--card-border);
    box-sizing: border-box;
    background: var(--paper);
  }
  .card--daniel { top: 17px; }
  .card--tom { top: 602px; }

  .name-band {
    position: absolute;
    left: -1px;
    top: 53px;
    width: 617px;
    height: 74px;
    background: var(--brand-red);
    overflow: hidden;
  }
  .name {
    position: absolute;
    left: 49px;
    bottom: -7px;
    margin: 0;
    font-size: 49px;
    font-weight: 400;
    line-height: 1;
    color: var(--paper);
    letter-spacing: -0.5px;
    white-space: nowrap;
  }

  .details {
    position: absolute;
    left: 49px;
    top: 184px;
    margin: 0;
    font-size: 43px;
    line-height: 37px;
    letter-spacing: 0.2px;
  }
  .details span { display: block; }
  .email {
    position: absolute;
    left: 49px;
    top: 280px;
    margin: 0;
    font-size: 43px;
    line-height: 1.1;
    white-space: nowrap;
  }
  .email .domain { color: var(--brand-red); }

  .socials {
    position: absolute;
    right: 30px;
    margin: 0;
    padding: 0;
    list-style: none;
    text-align: right;
    font-size: 44px;
    white-space: nowrap;
  }
  .card--daniel .socials { top: 400px; line-height: 47px; }
  .card--tom .socials { top: 352px; line-height: 50px; }
  .socials .sep { padding: 0 8px; }

  .brand {
    position: absolute;
    left: 740px;
    top: 40px;
    width: 200px;
    text-align: center;
  }
  .brand-dot {
    display: block;
    margin: 0 auto;
  }
  .brand-name {
    display: block;
    margin-top: 22px;
    font-family: "Arimo", Arial, sans-serif;
    font-weight: 700;
    font-size: 16px;
    letter-spacing: -0.3px;
    color: var(--label-grey);
  }
</style>
</head>
<body>
<main class="sheet">

  <section class="card card--daniel">
    <div class="name-band"><h1 class="name">DANIEL OVERBECK</h1></div>
    <p class="details"><span>entrepreneur</span><span>07423158871</span></p>
    <p class="email">doverbeck@<span class="domain">vantelo-demo.com</span></p>
    <div class="brand">
      <svg class="brand-dot" width="180" height="180" viewBox="0 0 180 180" aria-hidden="true">
        <circle cx="90" cy="90" r="86" fill="var(--brand-red)"/>
      </svg>
      <span class="brand-name">VANTELO COMPANY</span>
    </div>
    <ul class="socials">
      <li>friendhub<span class="sep">|</span>vantelo</li>
      <li>workline<span class="sep">|</span>danieloverbeck</li>
      <li>callspot<span class="sep">|</span>doverbeck</li>
    </ul>
  </section>

  <section class="card card--tom">
    <div class="name-band"><h1 class="name">TOM ASHWORTH</h1></div>
    <p class="details"><span>founder</span><span>07539402217</span></p>
    <p class="email">tashworth@<span class="domain">vantelo-demo.com</span></p>
    <div class="brand">
      <svg class="brand-dot" width="180" height="180" viewBox="0 0 180 180" aria-hidden="true">
        <circle cx="90" cy="90" r="86" fill="var(--brand-red)"/>
      </svg>
      <span class="brand-name">VANTELO COMPANY</span>
    </div>
    <ul class="socials">
      <li>friendhub<span class="sep">|</span>vantelo</li>
      <li>circle talk<span class="sep">|</span>tomashworth</li>
      <li>workline<span class="sep">|</span>thomasashworth</li>
      <li>callspot<span class="sep">|</span>thomasashworth</li>
    </ul>
  </section>

</main>
</body>
</html>
```